Vocational Mentor needs an impressive business card

1. I need a business card (or maybe three with identic look) to promote me and my three business titles/services:
- Vocational Mentor. I help people find their vocation and live happily from it. I use my 20 years of experience in business, management and psychology to help them identify the most efficient ways to make a living doing what they are passionate about.
- Business Angel. I help founders start a succesful business with minimum risks and costs. I use my 20 years of experience in sales, management and entrepreneurship to help them identify the most efficient ways, in terms of time and cost, to validate their business idea.
- Learning Designer. I design unique learning programs that produce long-term cognitive and behavioural changes to people and organisations. I use my 20 years of experience in learning, teaching and change management to create minimalist experiences and processes that allow them to change efficiently in their pursued direction.

2. I would like a two-sided business card, on the front with my name, contact details and titles, on the back the explanation of the services.
Updates

Hi all,

I updated my brief, included contacts info and give feedback on all designs I got. I am new on this platform so please tell me if you need anything else or if I don't use corectly the platform forms.

Kind regards,
Tudor

Hi all,

I shortened the services description by deleting the phrase "I call..."

Kind regards,
Tudor

Target Market(s)

Freelancers, startups, people and organization willing to invest in change through ultimate learning experiences

Industry/Entity Type

Business

Font styles to use
Serif

Requirements
Must have
• Front side: full name, titles, web site, email, phone like below:
Tudor Vasilache
Vocational Mentor, Business Angel, Learning Designer
info@tudorvasilache.example
www.tudorvasilache.example
+40-745-TUDORV
Nice to have
• Back side: the description of the services I provide as in the task description.
1/3: it would be nice if I can jam all three titles on the front side but then I need a solution to jam all three services on the back side.

```html
<!DOCTYPE html>
<html lang="en">
<head>
<meta charset="utf-8">
<title>Tudor Vasilache – Business Card</title>
<link rel="stylesheet" href="https://fonts.googleapis.com/css2?family=Cinzel:wght@400;700&family=Source+Sans+3:wght@400;600&display=swap">
<style>
  :root {
    --bg: #d9d9db;
    --card: #f7f7f6;
    --ink: #1e1e1e;
    --ink-soft: #333333;
    --blue: #1b87d2;
    --green: #6db52d;
    --orange: #ee6a1c;
    --shadow: rgba(0, 0, 0, 0.18);
  }
  * { box-sizing: border-box; margin: 0; padding: 0; }
  html, body {
    width: 1200px;
    height: 900px;
    overflow: hidden;
    background: var(--bg);
  }
  .canvas {
    position: relative;
    width: 1200px;
    height: 900px;
  }
  .card {
    position: absolute;
    width: 560px;
    height: 320px;
    background: var(--card);
    box-shadow: 0 6px 18px var(--shadow);
  }
  .accent-blue { color: var(--blue); }
  .accent-green { color: var(--green); }
  .accent-orange { color: var(--orange); }

  /* Back side – services */
  .card--back {
    left: 80px;
    top: 110px;
    padding: 34px 34px 0 34px;
  }
  .service {
    position: relative;
    padding-left: 60px;
    margin-bottom: 14px;
    font-family: "Source Sans 3", sans-serif;
    font-size: 13.5px;
    line-height: 1.28;
    color: var(--ink-soft);
  }
  .service__title {
    font-family: "Cinzel", serif;
    font-weight: 700;
    font-size: 14px;
    letter-spacing: 0.02em;
  }
  .service__marker {
    position: absolute;
    left: 14px;
    top: 6px;
    width: 22px;
    height: 22px;
    border-radius: 50%;
  }
  .service--mentor .service__marker { background: var(--blue); }
  .service--angel .service__marker { background: var(--green); }
  .service--designer .service__marker { background: var(--orange); }

  /* Front side – identity */
  .card--front {
    left: 560px;
    top: 470px;
  }
  .titles {
    position: absolute;
    left: 30px;
    top: 88px;
    width: 196px;
    text-align: right;
    font-family: "Cinzel", serif;
    font-size: 16px;
    line-height: 1.2;
    color: var(--ink);
  }
  .titles strong { font-weight: 700; }
  .titles__brace {
    position: absolute;
    left: 230px;
    top: 74px;
  }
  .name {
    position: absolute;
    left: 262px;
    top: 84px;
    font-family: "Cinzel", serif;
    font-weight: 700;
    font-size: 25px;
    letter-spacing: 0.01em;
    color: var(--ink);
  }
  .mark {
    position: absolute;
    left: 392px;
    top: 146px;
    width: 110px;
    height: 110px;
    border-radius: 50%;
    background: var(--green);
  }
  .contact {
    position: absolute;
    left: 30px;
    top: 196px;
    font-family: "Source Sans 3", sans-serif;
    font-size: 15px;
    line-height: 1.3;
    color: var(--ink);
    list-style: none;
  }
  .contact__phone { padding-left: 88px; }
</style>
</head>
<body>
<main class="canvas">

  <section class="card card--back" aria-label="Business card, back side">
    <p class="service service--mentor">
      <span class="service__marker"></span>
      <span class="service__title accent-blue">Vocational Mentor</span> – I help people to find their vocation and live happily from it. I use my 20 years of experience in business, management and psychology to help them identify the most efficient ways to make a living doing what they are passionate about.
    </p>
    <p class="service service--angel">
      <span class="service__marker"></span>
      <span class="service__title accent-green">Business Angel</span> – I help founders to start a successful business with minimum risks and costs. I use my 20 years of experience in sales, management and entrepreneurship to help them identify the most efficient ways, in terms of time and cost, to validate their business idea.
    </p>
    <p class="service service--designer">
      <span class="service__marker"></span>
      <span class="service__title accent-orange">Learning Designer</span> – I design unique learning programs that produce long-term cognitive and behavioural changes to people and organisations. I use my 20 years of experience in learning, teaching and change management to create minimalist experiences and processes that allows them to change efficiently in their pursued direction.
    </p>
  </section>

  <section class="card card--front" aria-label="Business card, front side">
    <p class="titles">
      Vocational <strong class="accent-blue">Mentor</strong><br>
      Business <strong class="accent-green">Angel</strong><br>
      Learning <strong class="accent-orange">Designer</strong>
    </p>
    <svg class="titles__brace" width="24" height="76" viewBox="0 0 24 76" aria-hidden="true">
      <path d="M3 2 C14 2 12 10 12 20 C12 30 12 36 21 38 C12 40 12 46 12 56 C12 66 14 74 3 74"
            fill="none" stroke="#555" stroke-width="1.4"/>
    </svg>
    <h1 class="name">Tudor Vasilache</h1>
    <span class="mark" aria-hidden="true"></span>
    <ul class="contact">
      <li>info@tudorvasilache.example</li>
      <li>www.tudorvasilache.example</li>
      <li class="contact__phone">+40-745-TUDORV</li>
    </ul>
  </section>

</main>
</body>
</html>
```